I need a business card for my new bakery - Mill Lane Oven Co. We make biscuits, cakes, muffins and other sweets. Our food is honest, wholesome and down to earth - i'd love this to be reflected in the design of the card. The design MUST include our logo (see the attached image - which needs to be replicated). The design should only use 2 or at most 3 colours.

Industry/Entity Type

Bakery

Requirements
Must have
• Must include my logo.
Must have a clean, simple design.
Space for my name, my title, my phone number, my facebook page (I will provide details later)
Should not have
• Must not have lots of bright colours.
Must not have any unnescassry graphics.

```html
<!DOCTYPE html>
<html lang="en">
<head>
<meta charset="utf-8">
<title>Mill Lane Oven Co — Business Card</title>
<link rel="stylesheet" href="https://fonts.googleapis.com/css2?family=Open+Sans:wght@400;700;800&display=swap">
<style>
  :root {
    --page-bg: #ece7e2;
    --card-light: #86501a;
    --card-mid: #774310;
    --card-dark: #5f330a;
    --ink-gold: #e9b820;
  }
  * { box-sizing: border-box; margin: 0; padding: 0; }
  html, body {
    width: 1200px;
    height: 833px;
    overflow: hidden;
    background: var(--page-bg);
    font-family: "Open Sans", Arial, sans-serif;
  }
  .sheet {
    width: 1200px;
    height: 833px;
    display: flex;
    justify-content: center;
    align-items: center;
    gap: 90px;
  }
  .card {
    position: relative;
    width: 350px;
    height: 610px;
    background: radial-gradient(ellipse at 50% 45%, var(--card-light) 0%, var(--card-mid) 55%, var(--card-dark) 100%);
    color: var(--ink-gold);
    text-align: center;
    box-shadow: 0 6px 18px rgba(0, 0, 0, 0.25);
  }
  .wordmark {
    position: absolute;
    top: 62px;
    left: 0;
    right: 0;
    font-weight: 800;
    font-size: 19px;
    letter-spacing: 0.06em;
    text-transform: uppercase;
  }
  .tagline {
    position: absolute;
    top: 232px;
    left: 0;
    right: 0;
    font-size: 31px;
    line-height: 1.36;
    font-weight: 400;
  }
  .tagline strong { font-weight: 800; }
  .tagline .closing { font-size: 37px; }
  .contact {
    position: absolute;
    top: 208px;
    left: 0;
    right: 0;
  }
  .contact-name {
    font-weight: 800;
    font-size: 16px;
    letter-spacing: 0.04em;
  }
  .contact-phone {
    font-size: 15px;
    letter-spacing: 0.02em;
  }
  .web-address {
    position: absolute;
    bottom: 48px;
    left: 0;
    right: 0;
    font-size: 17px;
    font-weight: 400;
  }
  .web-address strong { font-weight: 800; }
</style>
</head>
<body>
  <main class="sheet">
    <section class="card card-front">
      <div class="wordmark">Mill Lane Oven Co</div>
      <p class="tagline">
        We <strong>MAKE</strong><br>
        Biscuits<br>
        <strong>Cakes</strong><br>
        Muffins<br>
        and<br>
        <strong class="closing">other sweets</strong>
      </p>
    </section>
    <section class="card card-back">
      <div class="wordmark">Mill Lane Oven Co</div>
      <div class="contact">
        <p class="contact-name">SAM HARLOW</p>
        <p class="contact-phone">010 2468 135</p>
      </div>
      <p class="web-address">www.millaneoven.co/<strong>bakery</strong></p>
    </section>
  </main>
</body>
</html>
```